Bright Towns Alliance PowerPoint Design Template and Sample Deck

The Bright Towns Alliance is an international organization that seeks to improve the livability, workability and sustainability of the world’s cities.
We seek a versatile PowerPoint design template with 10 slide types plus a “self-documenting” sample deck. Your design will be used in keynote speeches and workshops around the world.
After the contest is completed, we will ask the winning designer to add 10-20 additional slide types for $75 per slide. We also seek a long-term relationship whereby we can request “custom” slides and/or ask the designer to touch up the slides we build to make them better.
FILES. We have uploaded several files:
1. BRIGHT TOWNS ALLIANCE DESIGN CONTEST NOTES.docx with full instructions.
2. PALETTE. Shows our official colors.
3 LOGOS. Several individual files with different variations of our logo. Some with our motto, some without.
2. SAMPLE SLIDES. Because we were unable to successfully upload our sample deck, we are making it available via this FileCrate link:
https://www.filecrate-example.net/s/k7qvmr2tn8wzd4h/The%20Bright%20Towns%20Alliance%20Design%20Contest%20Notes.docx?dl=0
Target Market(s)
Mayors, department heads, CIOs, senior executives from technology companies
Industry/Entity Type
Information Technology
Colors
Designer to choose colors to be used in the design.
Requirements
Must have
- Please see uploaded Word document for requirements, nice to haves and should not haves and uploaded palette for color preferences.
Nice to have
- see above
Should not have
- see above

```html
<!DOCTYPE html>
<html lang="en">
<head>
<meta charset="utf-8">
<title>Bright Towns Alliance – Individual Slides 01a</title>
<link href="https://fonts.googleapis.com/css2?family=Roboto:wght@700;900&family=Roboto+Condensed:wght@300;400&family=Open+Sans:ital,wght@0,400;0,600;0,700;1,400&display=swap" rel="stylesheet">
<style>
  :root{
    --rose:#e0bcbc;
    --note:#555555;
    --stage:#a8956f;
    --navy:#0f2b57;
    --blue:#2a5db0;
    --sky:#4f82c8;
    --purple:#7b4fa8;
    --green:#6a9a2e;
    --grey:#9a9a9a;
    --orange:#f0921c;
    --red:#e2572a;
    --gold:#f2b619;
    --paper:#f7f7f7;
    --ink:#444444;
  }
  *{margin:0;padding:0;box-sizing:border-box}
  html,body{width:1200px;height:1200px;overflow:hidden;background:#ffffff}
  .sheet{position:relative;width:1200px;height:1200px;font-family:"Open Sans",sans-serif}
  .sheet-title{position:absolute;top:58px;left:0;width:1200px;text-align:center;font-family:"Roboto",sans-serif;font-weight:900;font-size:66px;letter-spacing:1px;color:var(--rose)}
  .sheet-subtitle{position:absolute;top:142px;left:0;width:1200px;text-align:center;font-family:"Roboto Condensed",sans-serif;font-weight:300;font-size:29px;color:var(--rose)}
  .sheet-note{position:absolute;top:334px;left:24px;font-family:"Roboto Condensed",sans-serif;font-weight:300;font-size:18px;color:var(--note)}
  .note-arrow{position:absolute;top:365px;left:50px}
  .stage{position:absolute;top:414px;left:10px;width:1180px;height:662px;background:var(--stage)}
  .slide{position:absolute;width:314px;height:176px;box-shadow:3px 4px 8px rgba(0,0,0,.35)}
  .slide svg{display:block;width:314px;height:176px}
  .col-1{left:80px}.col-2{left:448px}.col-3{left:816px}
  .row-1{top:446px}.row-2{top:648px}.row-3{top:855px}
  svg text{font-family:"Open Sans",sans-serif}
  .s-title{font-size:10.5px;font-weight:600;fill:var(--blue)}
  .s-label{font-size:4px;fill:var(--ink)}
  .s-desc{font-size:2.6px;fill:#888888}
  .s-num{font-size:5px;font-weight:600}
  .foot-brand{font-size:8.5px;fill:#ffffff}
  .foot-meta{font-size:3.2px;fill:#ffffff}
  .brand-big{font-size:20px;fill:var(--navy)}
</style>
</head>
<body>
<div class="sheet">
  <h1 class="sheet-title">INDIVIDUAL SLIDES - 01a</h1>
  <p class="sheet-subtitle">(Bigger size for more details)</p>
  <p class="sheet-note">Please note that this title can be changed accordingly</p>
  <svg class="note-arrow" width="80" height="160" viewBox="0 0 80 160">
    <path d="M12 4 C4 40 6 90 20 120 C30 138 50 140 70 140" fill="none" stroke="#111" stroke-width="5" stroke-linecap="round"/>
    <path d="M54 126 L72 140 L52 152" fill="none" stroke="#111" stroke-width="5" stroke-linecap="round" stroke-linejoin="round"/>
  </svg>

  <div class="stage"></div>

  <!-- Slide: title -->
  <div class="slide col-1 row-1">
    <svg viewBox="0 0 314 176">
      <defs><linearGradient id="cityTone" x1="0" y1="0" x2="0" y2="1"><stop offset="0" stop-color="#2c63a8"/><stop offset="1" stop-color="#1d4f92"/></linearGradient></defs>
      <rect width="314" height="176" fill="url(#cityTone)" role="img" aria-label="Blue-toned photograph of a city skyline"/>
      <text x="51" y="80" font-size="19" font-weight="700" fill="#ffffff">The world is <tspan fill="var(--orange)">changing</tspan></text>
      <text x="157" y="103" text-anchor="middle" font-size="6.5" fill="#ffffff">“The biggest shift in economic gravity in history.”</text>
      <text x="185" y="112" text-anchor="middle" font-size="6.5" font-style="italic" fill="#ffffff">Harlow &amp; Finch</text>
    </svg>
  </div>

  <!-- Slide: section divider -->
  <div class="slide col-2 row-1">
    <svg viewBox="0 0 314 176">
      <rect width="314" height="176" fill="#7c4ea6"/>
      <rect x="30" y="-40" width="110" height="110" transform="rotate(30 85 15)" fill="#8a5cb3" opacity=".45"/>
      <rect x="40" y="60" width="110" height="110" transform="rotate(30 95 115)" fill="#6d4396" opacity=".45"/>
      <text x="272" y="89" text-anchor="end" font-size="8" font-weight="600" fill="#ffffff">1 Progressive Agenda</text>
      <text x="272" y="97" text-anchor="end" font-size="5" font-style="italic" fill="#e6dcef">Slide Ideas...</text>
      <circle cx="285" cy="86" r="5" fill="none" stroke="#ffffff" stroke-width=".8"/>
      <path d="M283.5 83.5 L287.5 86 L283.5 88.5Z" fill="none" stroke="#ffffff" stroke-width=".7"/>
    </svg>
  </div>

  <!-- Slide: rising bars -->
  <div class="slide col-3 row-1">
    <svg viewBox="0 0 314 176">
      <rect width="314" height="176" fill="var(--paper)"/>
      <text class="s-title" x="157" y="16" text-anchor="middle">Progressive Agenda</text>
      <g fill="var(--blue)"><rect x="150" y="24" width="2" height="2"/><rect x="153" y="24" width="2" height="2"/><rect x="156" y="24" width="2" height="2"/><rect x="159" y="24" width="2" height="2"/><rect x="162" y="24" width="2" height="2"/></g>
      <g>
        <rect x="27" y="119" width="30" height="36" fill="var(--purple)"/><path d="M57 119 l7 -6 v36 l-7 6z" fill="#5e3a85"/><path d="M27 119 l7 -6 h30 l-7 6z" fill="#9a74c2"/>
        <circle cx="47" cy="109" r="4" fill="var(--purple)"/><text class="s-num" x="47" y="111" text-anchor="middle" font-size="3" fill="#fff">01</text>
        <text x="42" y="130" text-anchor="middle" font-size="3" fill="#fff">Your Text</text>
        <text class="s-label" x="43" y="84" text-anchor="middle">Your Agenda - 01</text>
        <text class="s-desc" x="43" y="90" text-anchor="middle">Brief note on this item</text>
      </g>
      <g>
        <rect x="82" y="106" width="30" height="49" fill="var(--green)"/><path d="M112 106 l7 -6 v49 l-7 6z" fill="#4f7a1f"/><path d="M82 106 l7 -6 h30 l-7 6z" fill="#8cbb4c"/>
        <circle cx="102" cy="96" r="4" fill="var(--green)"/><text x="102" y="98" text-anchor="middle" font-size="3" fill="#fff">02</text>
        <text x="97" y="118" text-anchor="middle" font-size="3" fill="#fff">Your Text</text>
        <text class="s-label" x="98" y="77" text-anchor="middle">Your Agenda - 02</text>
        <text class="s-desc" x="98" y="83" text-anchor="middle">Brief note on this item</text>
      </g>
      <g>
        <rect x="137" y="94" width="30" height="61" fill="var(--grey)"/><path d="M167 94 l7 -6 v61 l-7 6z" fill="#777"/><path d="M137 94 l7 -6 h30 l-7 6z" fill="#bbb"/>
        <circle cx="157" cy="84" r="4" fill="var(--grey)"/><text x="157" y="86" text-anchor="middle" font-size="3" fill="#fff">03</text>
        <text x="152" y="106" text-anchor="middle" font-size="3" fill="#fff">Your Text</text>
        <text class="s-label" x="153" y="68" text-anchor="middle">Your Agenda - 03</text>
        <text class="s-desc" x="153" y="74" text-anchor="middle">Brief note on this item</text>
      </g>
      <g>
        <rect x="192" y="84" width="30" height="71" fill="var(--orange)"/><path d="M222 84 l7 -6 v71 l-7 6z" fill="#c9720c"/><path d="M192 84 l7 -6 h30 l-7 6z" fill="#f6b45a"/>
        <circle cx="212" cy="74" r="4" fill="var(--orange)"/><text x="212" y="76" text-anchor="middle" font-size="3" fill="#fff">04</text>
        <text x="207" y="96" text-anchor="middle" font-size="3" fill="#fff">Your Text</text>
        <text class="s-label" x="208" y="59" text-anchor="middle">Your Agenda - 04</text>
        <text class="s-desc" x="208" y="65" text-anchor="middle">Brief note on this item</text>
      </g>
      <g>
        <rect x="246" y="76" width="30" height="79" fill="var(--sky)"/><path d="M276 76 l7 -6 v79 l-7 6z" fill="#34639f"/><path d="M246 76 l7 -6 h30 l-7 6z" fill="#86aee0"/>
        <circle cx="266" cy="66" r="4" fill="var(--sky)"/><text x="266" y="68" text-anchor="middle" font-size="3" fill="#fff">05</text>
        <text x="261" y="88" text-anchor="middle" font-size="3" fill="#fff">Your Text</text>
        <text class="s-label" x="262" y="50" text-anchor="middle">Your Agenda - 05</text>
        <text class="s-desc" x="262" y="56" text-anchor="middle">Brief note on this item</text>
      </g>
      <rect y="158" width="314" height="18" fill="var(--navy)"/>
      <text class="foot-brand" x="11" y="170">Bright Towns Alliance</text>
      <text class="foot-meta" x="285" y="169" text-anchor="end">Bright Towns Alliance | Copyright 2017</text>
      <circle cx="294" cy="167" r="3.5" fill="var(--blue)"/><text x="294" y="168.3" text-anchor="middle" font-size="3.5" fill="#fff">5</text>
    </svg>
  </div>

  <!-- Slide: chevron timeline -->
  <div class="slide col-1 row-2">
    <svg viewBox="0 0 314 176">
      <rect width="314" height="176" fill="var(--paper)"/>
      <text class="s-title" x="157" y="16" text-anchor="middle">Progressive Agenda</text>
      <g fill="var(--blue)"><rect x="150" y="24" width="2" height="2"/><rect x="153" y="24" width="2" height="2"/><rect x="156" y="24" width="2" height="2"/><rect x="159" y="24" width="2" height="2"/><rect x="162" y="24" width="2" height="2"/></g>
      <g class="s-label" text-anchor="middle">
        <text x="47" y="60">Your Agenda - 01</text><text x="102" y="60">Your Agenda - 02</text><text x="157" y="60">Your Agenda - 03</text><text x="212" y="60">Your Agenda - 04</text><text x="267" y="60">Your Agenda - 05</text>
      </g>
      <g class="s-desc" text-anchor="middle">
        <text x="47" y="67">Brief note on this item</text><text x="102" y="67">Brief note on this item</text><text x="157" y="67">Brief note on this item</text><text x="212" y="67">Brief note on this item</text><text x="267" y="67">Brief note on this item</text>
      </g>
      <path d="M24 82 h45 l6 5 l-6 5 h-45 l6 -5z" fill="var(--purple)"/>
      <path d="M79 82 h45 l6 5 l-6 5 h-45 l6 -5z" fill="var(--orange)"/>
      <path d="M134 82 h45 l6 5 l-6 5 h-45 l6 -5z" fill="var(--grey)"/>
      <path d="M189 82 h45 l6 5 l-6 5 h-45 l6 -5z" fill="var(--green)"/>
      <path d="M244 82 h45 l6 5 l-6 5 h-45 l6 -5z" fill="var(--sky)"/>
      <g fill="#fff"><circle cx="49" cy="87" r="1.6"/><circle cx="104" cy="87" r="1.6"/><circle cx="159" cy="87" r="1.6"/><circle cx="214" cy="87" r="1.6"/><circle cx="269" cy="87" r="1.6"/></g>
      <g stroke-width=".6" stroke-dasharray="1.5 1.2" fill="none">
        <line x1="49" y1="92" x2="49" y2="110" stroke="var(--purple)"/><line x1="104" y1="92" x2="104" y2="110" stroke="var(--orange)"/><line x1="159" y1="92" x2="159" y2="110" stroke="var(--grey)"/><line x1="214" y1="92" x2="214" y2="110" stroke="var(--green)"/><line x1="269" y1="92" x2="269" y2="110" stroke="var(--sky)"/>
      </g>
      <g fill="none" stroke-width="1">
        <circle cx="49" cy="124" r="14" stroke="var(--purple)"/><circle cx="104" cy="124" r="14" stroke="var(--orange)"/><circle cx="159" cy="124" r="14" stroke="var(--grey)"/><circle cx="214" cy="124" r="14" stroke="var(--green)"/><circle cx="269" cy="124" r="14" stroke="var(--sky)"/>
      </g>
      <g class="s-num" text-anchor="middle">
        <text x="49" y="126" fill="var(--purple)">01</text><text x="104" y="126" fill="var(--orange)">02</text><text x="159" y="126" fill="var(--grey)">03</text><text x="214" y="126" fill="var(--green)">04</text><text x="269" y="126" fill="var(--sky)">05</text>
      </g>
      <rect y="158" width="314" height="18" fill="var(--navy)"/>
      <text class="foot-brand" x="11" y="170">Bright Towns Alliance</text>
      <text class="foot-meta" x="285" y="169" text-anchor="end">Bright Towns Alliance | Copyright 2017</text>
      <circle cx="294" cy="167" r="3.5" fill="var(--blue)"/><text x="294" y="168.3" text-anchor="middle" font-size="3.5" fill="#fff">6</text>
    </svg>
  </div>

  <!-- Slide: icon grid -->
  <div class="slide col-2 row-2">
    <svg viewBox="0 0 314 176">
      <rect width="314" height="176" fill="var(--paper)"/>
      <text class="s-title" x="157" y="16" text-anchor="middle">Progressive Agenda</text>
      <g fill="var(--blue)"><rect x="150" y="24" width="2" height="2"/><rect x="153" y="24" width="2" height="2"/><rect x="156" y="24" width="2" height="2"/><rect x="159" y="24" width="2" height="2"/><rect x="162" y="24" width="2" height="2"/></g>
      <g>
        <rect x="35" y="44" width="22" height="22" rx="3" fill="#1d4f92"/><rect x="41" y="50" width="10" height="10" rx="1.5" fill="none" stroke="#fff" stroke-width=".9"/><path d="M44.5 52.5 l4 2.5 l-4 2.5z" fill="#fff"/>
        <rect x="35" y="81" width="22" height="22" rx="3" fill="#7ea6d8"/><circle cx="46" cy="92" r="5" fill="none" stroke="#fff" stroke-width=".9"/><circle cx="46" cy="92" r="2" fill="#fff"/>
        <rect x="35" y="118" width="22" height="22" rx="3" fill="#8a8a8a"/><path d="M42 133 l8 -8" stroke="#fff" stroke-width="1.6" stroke-linecap="round"/><circle cx="42" cy="133" r="2" fill="none" stroke="#fff" stroke-width=".8"/><circle cx="50" cy="125" r="2" fill="none" stroke="#fff" stroke-width=".8"/>
        <rect x="166" y="44" width="22" height="22" rx="3" fill="var(--orange)"/><rect x="171" y="51" width="12" height="8" rx="1" fill="none" stroke="#fff" stroke-width=".9"/>
        <rect x="166" y="81" width="22" height="22" rx="3" fill="var(--purple)"/><path d="M172 89 h10 l-5 7z" fill="none" stroke="#fff" stroke-width=".9"/>
        <rect x="166" y="118" width="22" height="22" rx="3" fill="var(--green)"/><circle cx="177" cy="129" r="5" fill="none" stroke="#fff" stroke-width=".9"/><circle cx="177" cy="129" r="1.8" fill="#fff"/>
      </g>
      <g class="s-label"><text x="68" y="50">Your Agenda - 01</text><text x="68" y="87">Your Agenda - 02</text><text x="68" y="124">Your Agenda - 03</text><text x="199" y="50">Your Agenda - 04</text><text x="199" y="87">Your Agenda - 05</text><text x="199" y="124">Your Agenda - 06</text></g>
      <g class="s-desc"><text x="68" y="56">Brief note on this item</text><text x="68" y="93">Brief note on this item</text><text x="68" y="130">Brief note on this item</text><text x="199" y="56">Brief note on this item</text><text x="199" y="93">Brief note on this item</text><text x="199" y="130">Brief note on this item</text></g>
      <rect y="158" width="314" height="18" fill="var(--navy)"/>
      <text class="foot-brand" x="11" y="170">Bright Towns Alliance</text>
      <text class="foot-meta" x="285" y="169" text-anchor="end">Bright Towns Alliance | Copyright 2017</text>
      <circle cx="294" cy="167" r="3.5" fill="var(--blue)"/><text x="294" y="168.3" text-anchor="middle" font-size="3.5" fill="#fff">7</text>
    </svg>
  </div>

  <!-- Slide: staircase right -->
  <div class="slide col-3 row-2">
    <svg viewBox="0 0 314 176">
      <defs><linearGradient id="stairTone" x1="0" y1="1" x2="1" y2="0"><stop offset="0" stop-color="#4f82c8"/><stop offset=".35" stop-color="#f2b619"/><stop offset=".6" stop-color="#9a9a9a"/><stop offset=".8" stop-color="#e2572a"/><stop offset="1" stop-color="#1d4f92"/></linearGradient></defs>
      <rect width="314" height="176" fill="var(--paper)"/>
      <text class="s-title" x="157" y="22" text-anchor="middle">Progressive Agenda</text>
      <g fill="var(--blue)"><rect x="150" y="30" width="2" height="2"/><rect x="153" y="30" width="2" height="2"/><rect x="156" y="30" width="2" height="2"/><rect x="159" y="30" width="2" height="2"/><rect x="162" y="30" width="2" height="2"/></g>
      <g class="s-label" text-anchor="end"><text x="82" y="48">Your Agenda - 05</text><text x="82" y="73">Your Agenda - 04</text><text x="82" y="96">Your Agenda - 03</text><text x="82" y="120">Your Agenda - 02</text><text x="82" y="142">Your Agenda - 01</text></g>
      <g class="s-desc" text-anchor="end"><text x="82" y="54">Brief note on this item</text><text x="82" y="79">Brief note on this item</text><text x="82" y="102">Brief note on this item</text><text x="82" y="126">Brief note on this item</text><text x="82" y="148">Brief note on this item</text></g>
      <g stroke="#cccccc" stroke-width=".4"><line x1="92" y1="51" x2="160" y2="51"/><line x1="92" y1="76" x2="150" y2="76"/><line x1="92" y1="99" x2="140" y2="99"/><line x1="92" y1="123" x2="130" y2="123"/><line x1="92" y1="145" x2="122" y2="145"/></g>
      <g fill="#555"><circle cx="92" cy="51" r=".9"/><circle cx="92" cy="76" r=".9"/><circle cx="92" cy="99" r=".9"/><circle cx="92" cy="123" r=".9"/><circle cx="92" cy="145" r=".9"/></g>
      <rect x="159" y="50" width="14" height="2" fill="var(--blue)"/><rect x="149" y="75" width="14" height="2" fill="var(--red)"/><rect x="139" y="98" width="14" height="2" fill="var(--grey)"/><rect x="129" y="122" width="14" height="2" fill="var(--gold)"/><rect x="121" y="144" width="14" height="2" fill="var(--sky)"/>
      <rect x="150" y="28" width="62" height="126" fill="url(#stairTone)" opacity=".85" role="img" aria-label="Illustration of coloured stair-step blocks rising to an upward arrow"/>
      <text class="brand-big" x="228" y="78">Bright</text>
      <text class="brand-big" x="228" y="99">Towns</text>
      <text class="brand-big" x="228" y="120">Alliance</text>
      <rect y="158" width="314" height="18" fill="var(--navy)"/>
      <text class="foot-brand" x="11" y="170">Bright Towns Alliance</text>
      <text class="foot-meta" x="285" y="169" text-anchor="end">Bright Towns Alliance | Copyright 2017</text>
      <circle cx="294" cy="167" r="3.5" fill="var(--blue)"/><text x="294" y="168.3" text-anchor="middle" font-size="3.5" fill="#fff">9</text>
    </svg>
  </div>

  <!-- Slide: staircase left -->
  <div class="slide col-1 row-3">
    <svg viewBox="0 0 314 176">
      <defs><linearGradient id="stairToneLeft" x1="1" y1="1" x2="0" y2="0"><stop offset="0" stop-color="#4f82c8"/><stop offset=".35" stop-color="#f2b619"/><stop offset=".6" stop-color="#9a9a9a"/><stop offset=".8" stop-color="#e2572a"/><stop offset="1" stop-color="#1d4f92"/></linearGradient></defs>
      <rect width="314" height="176" fill="var(--paper)"/>
      <text class="s-title" x="196" y="19" text-anchor="middle">Progressive Agenda</text>
      <g fill="var(--blue)"><rect x="189" y="27" width="2" height="2"/><rect x="192" y="27" width="2" height="2"/><rect x="195" y="27" width="2" height="2"/><rect x="198" y="27" width="2" height="2"/><rect x="201" y="27" width="2" height="2"/></g>
      <rect x="60" y="18" width="72" height="136" fill="url(#stairToneLeft)" opacity=".85" role="img" aria-label="Illustration of coloured stair-step blocks rising to an upward arrow"/>
      <text x="9" y="84" font-size="13" fill="var(--navy)">Bright</text>
      <text x="9" y="97" font-size="13" fill="var(--navy)">Towns</text>
      <text x="9" y="110" font-size="13" fill="var(--navy)">Alliance</text>
      <g font-size="4" fill="var(--ink)"><text x="96" y="50">05</text><text x="104" y="76">04</text><text x="116" y="100">03</text><text x="128" y="123">02</text><text x="138" y="146">01</text></g>
      <rect x="110" y="47.5" width="14" height="2" fill="var(--blue)"/><rect x="118" y="73.5" width="14" height="2" fill="var(--red)"/><rect x="130" y="97.5" width="14" height="2" fill="var(--grey)"/><rect x="142" y="120.5" width="14" height="2" fill="var(--gold)"/><rect x="152" y="143.5" width="14" height="2" fill="var(--sky)"/>
      <g stroke="#cccccc" stroke-width=".4"><line x1="140" y1="49" x2="210" y2="49"/><line x1="140" y1="75" x2="210" y2="75"/><line x1="150" y1="99" x2="210" y2="99"/><line x1="162" y1="122" x2="210" y2="122"/><line x1="172" y1="145" x2="210" y2="145"/></g>
      <g fill="#555"><circle cx="210" cy="49" r=".9"/><circle cx="210" cy="75" r=".9"/><circle cx="210" cy="99" r=".9"/><circle cx="210" cy="122" r=".9"/><circle cx="210" cy="145" r=".9"/></g>
      <g class="s-label"><text x="218" y="48">Your Agenda - 05</text><text x="218" y="74">Your Agenda - 04</text><text x="218" y="97">Your Agenda - 03</text><text x="218" y="121">Your Agenda - 02</text><text x="218" y="143">Your Agenda - 01</text></g>
      <g class="s-desc"><text x="218" y="54">Brief note on this item</text><text x="218" y="80">Brief note on this item</text><text x="218" y="103">Brief note on this item</text><text x="218" y="127">Brief note on this item</text><text x="218" y="149">Brief note on this item</text></g>
      <rect y="158" width="314" height="18" fill="var(--navy)"/>
      <text class="foot-brand" x="11" y="170">Bright Towns Alliance</text>
      <text class="foot-meta" x="285" y="169" text-anchor="end">Bright Towns Alliance | Copyright 2017</text>
      <circle cx="294" cy="167" r="3.5" fill="var(--blue)"/><text x="294" y="168.3" text-anchor="middle" font-size="3.5" fill="#fff">10</text>
    </svg>
  </div>

  <!-- Slide: city timeline -->
  <div class="slide col-2 row-3">
    <svg viewBox="0 0 314 176">
      <rect width="314" height="176" fill="var(--paper)"/>
      <text class="s-title" x="157" y="16" text-anchor="middle">Progressive Agenda</text>
      <g fill="var(--blue)"><rect x="150" y="24" width="2" height="2"/><rect x="153" y="24" width="2" height="2"/><rect x="156" y="24" width="2" height="2"/><rect x="159" y="24" width="2" height="2"/><rect x="162" y="24" width="2" height="2"/></g>
      <path d="M22 92 V62 H264" fill="none" stroke="var(--green)" stroke-width=".7"/>
      <circle cx="60" cy="62" r="11" fill="#8a8a8a"/><circle cx="60" cy="62" r="4" fill="none" stroke="#fff" stroke-width="1"/>
      <circle cx="128" cy="62" r="11" fill="var(--orange)"/><rect x="124" y="58" width="8" height="8" rx="1" fill="none" stroke="#fff" stroke-width="1"/>
      <circle cx="196" cy="62" r="11" fill="var(--orange)"/><rect x="192" y="59" width="8" height="6" rx="1" fill="none" stroke="#fff" stroke-width="1"/>
      <circle cx="264" cy="62" r="11" fill="var(--purple)"/><rect x="260" y="59" width="8" height="6" rx="1" fill="none" stroke="#fff" stroke-width="1"/>
      <g class="s-label" text-anchor="middle"><text x="62" y="83">Your Agenda - 01</text><text x="130" y="83">Your Agenda - 02</text><text x="198" y="83">Your Agenda - 03</text><text x="266" y="83">Your Agenda - 04</text></g>
      <g class="s-desc" text-anchor="middle"><text x="62" y="89">Brief note on this item</text><text x="130" y="89">Brief note on this item</text><text x="198" y="89">Brief note on this item</text><text x="266" y="89">Brief note on this item</text></g>
      <circle cx="22" cy="94" r="6" fill="var(--gold)" stroke="var(--blue)" stroke-width="1.2"/>
      <rect x="0" y="132" width="314" height="26" fill="var(--green)" role="img" aria-label="Green city skyline silhouette"/>
      <rect x="10" y="100" width="30" height="58" fill="#f3c99a" opacity=".7" role="img" aria-label="Drawn hand pressing a button"/>
      <text x="48" y="110" font-size="7" fill="var(--navy)">Bright</text>
      <text x="48" y="117" font-size="7" fill="var(--navy)">Towns</text>
      <text x="48" y="124" font-size="7" fill="var(--navy)">Alliance</text>
      <rect y="158" width="314" height="18" fill="var(--navy)"/>
      <text class="foot-brand" x="11" y="170">Bright Towns Alliance</text>
      <text class="foot-meta" x="285" y="169" text-anchor="end">Bright Towns Alliance | Copyright 2017</text>
      <circle cx="294" cy="167" r="3.5" fill="var(--blue)"/><text x="294" y="168.3" text-anchor="middle" font-size="3.5" fill="#fff">11</text>
    </svg>
  </div>
</div>
</body>
</html>
```